QRV-TB 2018 Recycling Rate Report

We need a design for our 2018 Recycling Rate Report on Expanded Polystyrene. We want to move from a larger booklet style to a two page document. The report from last year - which was done as a booklet - is attached to provide an example of our style and design.The primary items that must be included (but not limited to) the information on pages 3, 5 & 7. The graphs must include room for 2018 data.To view our typical company design/style please see our website at www.qrvtradeboard.org. Our primary RGB colors are: (187,140,9); (94,47,29); (94,138,164); and (164,167,15). Secondary RGB colors are (249,162,28) and (218,210,208). Our title/header font is DIN Next LT Pro and our copy font is Calibri 10.5 pt. We can deviate from the font specification if beneficial and welcome interesting text treatments and typography.

Target Market(s)

Recycling facilities & general public.

Font styles to use
Sans Serif

Requirements
Must have
• Information presentation must be clean and easy to reference.

```html
<!DOCTYPE html>
<html lang="en">
<head>
<meta charset="utf-8">
<title>QRV-TB 2018 Recycling Rate Report</title>
<link rel="stylesheet" href="https://fonts.googleapis.com/css2?family=Carlito:wght@400;700&family=Montserrat:wght@300;400;700&display=swap">
<style>
  :root{
    --gold:#bb8c09;
    --blue:#5e8aa4;
    --olive:#a4a70f;
    --line:#9f9a36;
    --orange:#f9a21c;
    --stone:#dad2d0;
    --ink:#1c1c1c;
    --white:#ffffff;
    --grid:#d9d9d9;
    --muted:#b9b9b9;
  }
  *{margin:0;padding:0;box-sizing:border-box}
  html,body{width:927px;height:1200px;overflow:hidden}
  body{background:var(--stone);font-family:"Carlito",Calibri,sans-serif;color:var(--ink);position:relative}
  .panel{position:absolute;top:0;height:454px}
  .panel--method{left:0;width:463px;background:var(--gold);color:var(--white);padding:58px 78px 0 38px}
  .panel--collect{left:463px;width:464px;background:var(--blue);color:var(--ink);padding:30px 88px 0 27px}
  .panel h2{font-family:"Montserrat",sans-serif;font-weight:300;letter-spacing:.5px;font-size:31px;line-height:29px;white-space:nowrap}
  .panel--method h2{margin-bottom:30px}
  .panel--collect h2{margin-bottom:27px}
  .panel p{font-size:15px;line-height:19.7px}
  .photo{position:absolute;top:477px;width:192px;height:146px}
  .photo--industrial{left:23px;background:linear-gradient(135deg,#4a4b4d,#d9dbdc 55%,#f2f2f2)}
  .photo--consumer{left:257px;background:linear-gradient(160deg,#3d3a36,#8a8884 45%,#bfc2c3)}
  .summary{position:absolute;left:486px;top:491px;width:390px;font-size:15.2px;line-height:19.2px;color:var(--ink)}
  .stat{position:absolute;top:630px;width:220px;text-align:center}
  .stat--industrial{left:10px}
  .stat--consumer{left:244px}
  .stat h3{font-family:"Montserrat",sans-serif;font-weight:400;font-size:20px;line-height:24px}
  .stat small{display:block;font-family:"Montserrat",sans-serif;font-size:9.5px;line-height:11px}
  .stat strong{display:block;font-family:"Montserrat",sans-serif;font-weight:700;font-size:68px;line-height:66px;letter-spacing:-1px}
  .stat--industrial strong{color:var(--orange)}
  .stat--consumer strong{color:var(--olive)}
  .chart-title{position:absolute;left:0;width:927px;top:746px;text-align:center;font-family:"Montserrat",sans-serif;font-weight:400;font-size:22px;letter-spacing:.3px}
  .chart{position:absolute;left:49px;top:783px;width:829px;height:382px;background:var(--white)}
  .chart svg{display:block}
  .chart text{font-family:"Montserrat",sans-serif}
</style>
</head>
<body>
  <section class="panel panel--method">
    <h2>METHODOLOGY</h2>
    <p>The 2018 Expanded Polystyrene Recycling Rate Study was conducted by the QRV Trade Board to gather data to reflect both post-consumer and post-industrial recycling activity. The 2018 results are based on data received from 55 EPS manufacturers and independent recyclers in the U.S.</p>
    <p>Participation in the EPS recycling survey is voluntary and the reported data is based on the responses received. Many companies have limited resources to put towards participation in the survey, and some companies may choose not to respond due to their confidentiality policies. Therefore, because there is not 100 percent participation, the presented totals represent the minimum amount of EPS recovered for recycling.</p>
  </section>

  <section class="panel panel--collect">
    <h2>COLLECTION OPTIONS<br>&amp; RESOURCES</h2>
    <p>Not everything can be recycled all the time. In order for materials to be recycled, stable markets must exist and there must be a demand for the end products. Each community has its own guidelines for which plastics are accepted, and these can vary widely. Some locations also offer consumer dropoff access. To find out if EPS recycling is available in your area, visit www.qrvtradeboard.org.</p>
    <p>For consumers that do not have access to a local drop-off center, the QRV-TB sponsors a National Mail-Back Program intended for smaller quantities of EPS which can be mailed via NPX Post or ParcelRun to more than 20 locations nationwide. Full instructions and a list of Mail-Back locations are available on the QRV-TB website.</p>
  </section>

  <div class="photo photo--industrial" role="img" aria-label="Worker sorting piles of white post-industrial foam packaging"></div>
  <div class="photo photo--consumer" role="img" aria-label="Person dropping a large foam sheet into a recycling bin"></div>

  <p class="summary">The 25-year baseline shows incremental gains with more than 23 million pounds of EPS recycled annually on average. Like all commodity markets, the EPS recycling market is cyclical. The 2017 results reflect a decrease from 2016 due to the new landscape for recycling commodities and changing international markets, especially in China.</p>

  <div class="stat stat--industrial">
    <h3>Post-Industrial</h3>
    <small>(millions of pounds)</small>
    <strong>39.0</strong>
  </div>
  <div class="stat stat--consumer">
    <h3>Post-Consumer</h3>
    <small>(millions of pounds)</small>
    <strong>25.9</strong>
  </div>

  <h2 class="chart-title">Post-Consumer EPS Recycling 1990-2018</h2>

  <figure class="chart">
    <svg width="829" height="382" viewBox="0 0 1140 525" aria-label="Line chart of post-consumer EPS recycling from 1990 to 2018">
      <g stroke="var(--grid)" stroke-width="1.2">
        <line x1="177" y1="26" x2="177" y2="498"/><line x1="244" y1="26" x2="244" y2="498"/>
        <line x1="311" y1="26" x2="311" y2="498"/><line x1="378" y1="26" x2="378" y2="498"/>
        <line x1="445" y1="26" x2="445" y2="498"/><line x1="512" y1="26" x2="512" y2="498"/>
        <line x1="579" y1="26" x2="579" y2="498"/><line x1="646" y1="26" x2="646" y2="498"/>
        <line x1="713" y1="26" x2="713" y2="498"/><line x1="780" y1="26" x2="780" y2="498"/>
        <line x1="847" y1="26" x2="847" y2="498"/><line x1="914" y1="26" x2="914" y2="498"/>
        <line x1="981" y1="26" x2="981" y2="498"/><line x1="1048" y1="26" x2="1048" y2="498"/>
      </g>
      <g stroke="var(--muted)" stroke-width="1.2">
        <line x1="103" y1="30" x2="103" y2="472"/>
        <line x1="96" y1="40" x2="103" y2="40"/><line x1="96" y1="102" x2="103" y2="102"/>
        <line x1="96" y1="163" x2="103" y2="163"/><line x1="96" y1="225" x2="103" y2="225"/>
        <line x1="96" y1="287" x2="103" y2="287"/><line x1="96" y1="349" x2="103" y2="349"/>
        <line x1="96" y1="410" x2="103" y2="410"/><line x1="96" y1="472" x2="103" y2="472"/>
      </g>
      <g fill="var(--muted)" font-size="18" text-anchor="end">
        <text x="88" y="46">70</text><text x="88" y="108">60</text><text x="88" y="169">50</text>
        <text x="88" y="231">40</text><text x="88" y="293">30</text><text x="88" y="355">20</text>
        <text x="88" y="416">10</text><text x="88" y="478">0</text>
      </g>
      <text transform="translate(37 260) rotate(-90)" fill="var(--muted)" font-size="18" text-anchor="middle">Millions of Pounds Recycled</text>
      <g fill="var(--ink)" font-size="17" text-anchor="middle">
        <text x="143" y="497">1990</text><text x="210" y="497">1992</text><text x="277" y="497">1994</text>
        <text x="344" y="497">1996</text><text x="411" y="497">1998</text><text x="478" y="497">2000</text>
        <text x="545" y="497">2002</text><text x="612" y="497">2004</text><text x="679" y="497">2006</text>
        <text x="746" y="497">2008</text><text x="813" y="497">2010</text><text x="880" y="497">2012</text>
        <text x="947" y="497">2016</text><text x="1014" y="497">2017</text><text x="1081" y="497">2018</text>
      </g>
      <polyline fill="none" stroke="var(--line)" stroke-width="2" points="143,456 210,344 277,323 344,333 411,360 478,318 545,310 612,318 679,275 746,265 813,243 880,246 947,84 1014,310"/>
      <g fill="var(--line)">
        <circle cx="143" cy="456" r="6"/><circle cx="210" cy="344" r="6"/><circle cx="277" cy="323" r="6"/>
        <circle cx="344" cy="333" r="6"/><circle cx="411" cy="360" r="6"/><circle cx="478" cy="318" r="6"/>
        <circle cx="545" cy="310" r="6"/><circle cx="612" cy="318" r="6"/><circle cx="679" cy="275" r="6"/>
        <circle cx="746" cy="265" r="6"/><circle cx="813" cy="243" r="6"/><circle cx="880" cy="246" r="6"/>
        <circle cx="947" cy="84" r="6"/><circle cx="1014" cy="310" r="6"/>
      </g>
      <g fill="var(--ink)" font-size="17" text-anchor="middle">
        <text x="143" y="433">3.0</text><text x="210" y="323">20.8</text><text x="277" y="300">24.2</text>
        <text x="344" y="313">22.5</text><text x="411" y="339">18.2</text><text x="478" y="296">24.9</text>
        <text x="545" y="290">26.2</text><text x="612" y="297">25.0</text><text x="679" y="253">32.0</text>
        <text x="746" y="242">33.6</text><text x="813" y="222">37.1</text><text x="874" y="224">36.7</text>
        <text x="947" y="62">63.0</text><text x="1014" y="336">25.9</text>
      </g>
    </svg>
  </figure>
</body>
</html>
```